Sci fi cover needed for Brimbly/aMolder

I'd like a variation on the below design, I like the white logo with the colour blending in but this time with a different colour and different graphic below. No subtitle needed.

```html
<!DOCTYPE html>
<html lang="en">
<head>
<meta charset="utf-8">
<title>Faraway Colony Outpost – Cover</title>
<link rel="stylesheet" href="https://fonts.googleapis.com/css2?family=Anton&display=swap">
<style>
  :root {
    --space-deep: #0c0414;
    --space-mid: #2a0c3c;
    --nebula-magenta: #d13cc4;
    --nebula-violet: #7a2bd6;
    --horizon-glow: #ff8ae6;
    --planet-dark: #16071f;
    --title-white: #ffffff;
  }
  html, body {
    margin: 0;
    padding: 0;
    width: 1200px;
    height: 1200px;
    overflow: hidden;
    background: var(--space-deep);
  }
  .cover {
    position: relative;
    width: 1200px;
    height: 1200px;
    overflow: hidden;
    background:
      radial-gradient(circle at 20% 22%, rgba(209,60,196,0.28) 0, transparent 320px),
      radial-gradient(circle at 82% 30%, rgba(122,43,214,0.30) 0, transparent 360px),
      radial-gradient(ellipse at 50% 100%, rgba(255,138,230,0.35) 0, transparent 640px),
      linear-gradient(180deg, var(--space-deep) 0%, var(--space-mid) 60%, #3a0f4a 100%);
  }
  .scene {
    position: absolute;
    inset: 0;
    width: 1200px;
    height: 1200px;
  }
  .star { fill: #ffffff; }
  .title-main, .title-sub {
    font-family: "Anton", "Impact", sans-serif;
    fill: url(#titleBlend);
  }
</style>
</head>
<body>
  <main class="cover">
    <svg class="scene" viewBox="0 0 1200 1200" xmlns="http://www.w3.org/2000/svg" aria-label="Faraway Colony Outpost">
      <defs>
        <linearGradient id="titleBlend" x1="0" y1="0" x2="0" y2="1">
          <stop offset="0" stop-color="#ffffff"/>
          <stop offset="0.7" stop-color="#ffffff"/>
          <stop offset="1" stop-color="#ffc8f2"/>
        </linearGradient>
        <radialGradient id="planetBody" cx="0.5" cy="0" r="0.9">
          <stop offset="0" stop-color="#3b1150"/>
          <stop offset="1" stop-color="var(--planet-dark)"/>
        </radialGradient>
      </defs>

      <g class="stars">
        <circle class="star" cx="120" cy="140" r="2.5"/>
        <circle class="star" cx="310" cy="80" r="1.8"/>
        <circle class="star" cx="520" cy="190" r="2.2"/>
        <circle class="star" cx="760" cy="110" r="1.6"/>
        <circle class="star" cx="980" cy="170" r="2.6"/>
        <circle class="star" cx="1100" cy="320" r="1.8"/>
        <circle class="star" cx="70" cy="380" r="1.6"/>
        <circle class="star" cx="1140" cy="520" r="2"/>
        <circle class="star" cx="60" cy="640" r="2"/>
        <circle class="star" cx="420" cy="320" r="1.4"/>
        <circle class="star" cx="860" cy="300" r="1.5"/>
      </g>

      <g class="planet-horizon">
        <circle cx="600" cy="2250" r="1380" fill="none" stroke="var(--horizon-glow)" stroke-width="26" opacity="0.25"/>
        <circle cx="600" cy="2250" r="1370" fill="url(#planetBody)" stroke="var(--horizon-glow)" stroke-width="4"/>
        <ellipse cx="600" cy="930" rx="700" ry="70" fill="none" stroke="var(--nebula-magenta)" stroke-width="3" opacity="0.55"/>
      </g>

      <text class="title-main" x="168" y="640" font-size="226" textLength="864" lengthAdjust="spacingAndGlyphs">FARAWAY</text>
      <text class="title-sub" x="168" y="756" font-size="106" textLength="864" lengthAdjust="spacingAndGlyphs">COLONYOUTPOST</text>
    </svg>
  </main>
</body>
</html>
```